Style Template created - Report Accounting and Advisory industry

We need a style template created to set out a report for advice. The report follows <br/><br/>- Cover Page - ( we would need to print to a letter head )<br/>- General Disclaimer<br/>- Space to add Excel Reports in to the document- Maybe inserted Pdf's later<br/>- Action Plan dot points under headings<br/>- List of Strategies to be adopted<br/><br/>Attached is a quick example word doc that needs Custom Style Templates made so that we can quickly format items added. Also the ugly PDF that we currently produce for clients <br/><br/>Red - is our preferred Colour<br/><br/>

Target Market(s)

Accounting / Business / Professionals

Industry/Entity Type

Accounting

Colors
ec1f27

Requirements
Nice to have
• Simple Clean design. Not to busy. Easy to modify the "wording text" in design
Should not have
• Too busy or too much color

```html
<!DOCTYPE html>
<html lang="en">
<head>
<meta charset="utf-8">
<title>Taxation Projection and Planning 2020 – Report Template</title>
<link rel="stylesheet" href="https://fonts.googleapis.com/css2?family=Open+Sans:ital,wght@0,300;0,400;0,600;0,700;1,700&family=Arimo:ital,wght@0,400;0,700;1,700&family=Tinos:wght@400;700&family=Libre+Baskerville:ital,wght@1,700&display=swap">
<style>
  :root {
    --backdrop: #c6c7c9;
    --paper: #ffffff;
    --brand-red: #b5121b;
    --ink: #333333;
    --ink-soft: #555555;
    --band-grey: #e6e7e8;
    --bar-grey: #c8c9cb;
    --row-warm: #f5e1da;
    --row-pale: #faf2ee;
    --quote-pink: #fbecec;
  }
  * { margin: 0; padding: 0; box-sizing: border-box; }
  html, body { width: 1200px; height: 1200px; overflow: hidden; }
  body { background: var(--backdrop); position: relative; font-family: "Arimo", Arial, sans-serif; color: var(--ink); }

  .page {
    position: absolute; width: 413px; height: 584px; background: var(--paper);
    transform: scale(0.8136); transform-origin: 0 0; overflow: hidden;
  }
  .page--cover { left: 67px; top: 101px; }
  .page--disclaimer { left: 436px; top: 101px; }
  .page--purpose { left: 797px; top: 101px; }
  .page--excel { left: 67px; top: 625px; }
  .page--strategies { left: 436px; top: 625px; }

  .page__art { position: absolute; left: 0; top: 0; width: 413px; height: 584px; }

  .wordmark { position: absolute; left: 39px; font-family: "Open Sans", sans-serif; color: var(--brand-red); font-weight: 400; letter-spacing: .02em; line-height: 1; }
  .wordmark__tag { display: block; font-size: .3em; color: #999; letter-spacing: .04em; margin-top: 3px; }
  .page--cover .wordmark { top: 40px; font-size: 20px; }
  .page .wordmark--small { top: 21px; font-size: 12.5px; }

  .running-head { position: absolute; right: 38px; top: 27px; font-size: 5.5px; color: var(--ink-soft); }
  .footer-note { position: absolute; left: 39px; top: 555px; font-size: 5.5px; font-weight: 700; color: var(--brand-red); }
  .page-number { position: absolute; right: 29px; top: 554px; font-size: 7px; font-weight: 700; color: #fff; }

  .cover-title { position: absolute; left: 109px; top: 174px; font-family: "Open Sans", sans-serif; line-height: 1; }
  .cover-title__lead { display: block; font-size: 25px; font-weight: 700; color: var(--brand-red); }
  .cover-title__rest { display: block; font-size: 36px; font-weight: 300; color: #444; line-height: 1.02; }
  .cover-client { position: absolute; left: 109px; top: 340px; font-size: 11px; font-weight: 700; }
  .cover-url { position: absolute; right: 38px; top: 553px; font-size: 8px; font-weight: 700; }

  .body { position: absolute; left: 39px; width: 333px; font-size: 6.6px; line-height: 1.25; color: var(--ink); }
  .body p { margin-bottom: 7px; }
  .body h3 { font-size: 7px; font-weight: 700; }

  .disclaimer-title { position: absolute; left: 0; width: 413px; top: 127px; text-align: center; font-size: 11px; font-weight: 700; letter-spacing: .02em; }
  .signoff { position: absolute; left: 39px; top: 406px; font-size: 6.6px; line-height: 1.3; }

  .section-title { font-family: "Open Sans", sans-serif; font-size: 13px; font-weight: 700; color: var(--ink); margin-bottom: 2px; }
  .section-sub { font-size: 10px; font-style: italic; font-weight: 700; margin-bottom: 9px; }
  .section-head { font-family: "Open Sans", sans-serif; font-size: 10px; font-weight: 700; margin: 10px 0 5px; }
  .benefits { list-style: disc; padding-left: 11px; }
  .benefits li { margin-bottom: 1.5px; }
  .narrow { width: 172px; }

  .pull-quote { position: absolute; left: 224px; top: 345px; width: 165px; height: 110px; }
  .pull-quote__text { position: absolute; left: 16px; top: 22px; font-family: "Libre Baskerville", serif; font-style: italic; font-weight: 700; font-size: 15px; line-height: 1.5; color: var(--brand-red); }

  .excel-label { position: absolute; left: 39px; top: 63px; font-size: 10px; font-style: italic; font-weight: 700; }
  .excel-bar { position: absolute; left: 39px; width: 335px; }
  .excel-bar--head { top: 80px; height: 19px; background: var(--bar-grey); }
  .excel-bar--row { top: 99px; height: 12px; background: var(--band-grey); }

  .strategy-title { position: absolute; left: 39px; top: 65px; font-family: "Open Sans", sans-serif; font-size: 12.5px; font-weight: 700; font-style: italic; color: var(--brand-red); line-height: 1.45; }
  .strategy-label { position: absolute; left: 39px; top: 110px; font-family: "Open Sans", sans-serif; font-size: 12px; font-style: italic; color: #444; }
  .serif { font-family: "Tinos", "Times New Roman", serif; }
  .caps-head { position: absolute; left: 39px; font-size: 10px; letter-spacing: .02em; }
  .caps-note { position: absolute; left: 39px; font-size: 5px; }
  .strategy-table { position: absolute; left: 39px; top: 223px; width: 335px; font-size: 5px; line-height: 1.3; }
  .strategy-row { padding: 5px 7px 7px; }
  .strategy-row:nth-child(odd) { background: var(--row-warm); }
  .strategy-row:nth-child(even) { background: var(--row-pale); }
  .strategy-row h4 { font-weight: 700; font-size: 5px; margin-bottom: 6px; }
  .strategy-row p { margin-bottom: 6px; }
  .strategy-row ul { list-style: none; padding-left: 25px; margin-bottom: 6px; }
</style>
</head>
<body>

<!-- Cover -->
<section class="page page--cover">
  <svg class="page__art" viewBox="0 0 413 584" aria-hidden="true">
    <polygon points="75,584 413,365 413,584" fill="var(--band-grey)"/>
    <polygon points="0,508 158,401 158,478 0,584" fill="var(--brand-red)"/>
    <polygon points="158,478 413,310 413,360 158,530" fill="var(--brand-red)"/>
  </svg>
  <div class="wordmark">HARLOW BRENT<span class="wordmark__tag">CHARTERED ACCOUNTANTS</span></div>
  <h1 class="cover-title">
    <span class="cover-title__lead">TAXATION</span>
    <span class="cover-title__rest">PROJECTION<br>AND PLANNING<br>2020</span>
  </h1>
  <p class="cover-client">Client Name</p>
  <p class="cover-url">www.harlowbrent.com.au</p>
</section>

<!-- Disclaimer -->
<section class="page page--disclaimer">
  <svg class="page__art" viewBox="0 0 413 584" aria-hidden="true">
    <polygon points="230,584 363,495 363,520 268,584" fill="var(--band-grey)"/>
    <polygon points="385,508 413,490 413,512 385,530" fill="var(--band-grey)"/>
    <polygon points="302,584 413,510 413,584" fill="var(--brand-red)"/>
  </svg>
  <div class="wordmark wordmark--small">HARLOW BRENT<span class="wordmark__tag">CHARTERED ACCOUNTANTS</span></div>
  <p class="running-head">2020 Tax Planning | Client Name Here</p>
  <h2 class="disclaimer-title">DISCLAIMER</h2>
  <div class="body" style="top:160px">
    <p>The taxation estimate has been prepared on the basis of information provided by the client. The report Is intended for internal tax planning purposes and represents a "What if scenario". It does not necessarily represent real or intended transactions.</p>
    <p>HarlowBrent have not performed any tests to verify or validate any of the information provided by the client and accordingly express no assurance as to the outcome indicated.</p>
    <p>To the extent permitted by law we do not accept liability for any loss or damage which any person, other than the client may suffer arising from any negligence on our part. No person should rely on the Taxation estimate without having a full review or audit conducted on the data.</p>
    <h3>Superannuation</h3>
    <p>Provision of Advice is guided by legislative requirements to be provided in a Statement of Advice. Any and all comments regarding Superannuation are not to be taken as advice rather than statement of factual information about the situation. The statement is not a recommendation to take any action unless that action is required by law. The clients personal situation has not been considered in</p>
    <p>providing the information. Any action to be taken in relation to the information provided, should take into account the clients personal situation and consideration must be given as to whether action will be appropriate for the clients' objectives and needs. Specific Contribution amounts and SMSF product advice can only be provided under a Statement of Advice by a AFSL Holder.</p>
  </div>
  <p class="signoff"><strong>HarlowBrent</strong><br>Chartered Accountants</p>
  <p class="footer-note">© 2020 HarlowBrent&nbsp; Chartered Accountants</p>
  <p class="page-number">2</p>
</section>

<!-- Purpose -->
<section class="page page--purpose">
  <svg class="page__art" viewBox="0 0 413 584" aria-hidden="true">
    <polygon points="230,584 363,495 363,520 268,584" fill="var(--band-grey)"/>
    <polygon points="385,508 413,490 413,512 385,530" fill="var(--band-grey)"/>
    <polygon points="302,584 413,510 413,584" fill="var(--brand-red)"/>
  </svg>
  <div class="wordmark wordmark--small">HARLOW BRENT<span class="wordmark__tag">CHARTERED ACCOUNTANTS</span></div>
  <p class="running-head">2020 Tax Planning | Client Name Here</p>
  <div class="body" style="top:67px">
    <h2 class="section-title">Purpose of Tax Planning</h2>
    <p class="section-sub">Why bother.....???</p>
    <p>Tax planning is the activities taken to minimise tax liabilities to ensure all available allowances, deductions, exclusions and exemptions are working together in the most tax effective manner to reduce the total tax bill.</p>
    <p style="margin-bottom:16px">The purpose of this report is to provide a recommedation of strategies for you to consider for the year to come. This report is not intended to be our final advice to you, but instead a stating point in educating you on potential opportunities.</p>
    <p style="margin-bottom:2px">Tax planning strategies are typically employed to help a business achieve their financial and business goals. The benefits of tax planning are:</p>
    <ul class="benefits">
      <li>Lowering the Amount of taxable income</li>
      <li>Reduceing the tax rate</li>
      <li>Allowing greater Control of when taxes get paid</li>
      <li>Better Management of your cashflow</li>
      <li>Eliminating nasty tax surprises</li>
    </ul>
    <h3 class="section-head">Recommendations</h3>
    <p>We will provide you with a list of Action plans and a further list of ……… The list will be broken down in Short term and Longer Term action. Also list of actions to follow up on …..work on this bit ……sjc</p>
    <h3 class="section-head">Basis of Preparation</h3>
    <div class="narrow">
      <p>The taxation estimate has been prepared on the basis of information provided by the client. The report is intended for internal tax planning purposes and represents a "What if scenario". It does not necessarily represent real or intended transactions.</p>
      <p>HarlowBrent have not performed any tests to verify or validate any of the information provided by the client and accordingly express no assurance as to the outcome indicated.</p>
      <p>To the extent permitted by law we do not accept liability for any loss or damage which any person, other than the client may suffer arising from any negligence on our part. No person should rely on the Taxation estimate without having a full review or audit conducted on the data.</p>
    </div>
  </div>
  <figure class="pull-quote">
    <svg width="165" height="110" viewBox="0 0 165 110" aria-hidden="true">
      <polygon points="10,8 165,8 158,102 0,102" fill="var(--quote-pink)"/>
      <text x="2" y="16" font-family="Georgia, serif" font-weight="700" font-size="26" fill="var(--brand-red)">“</text>
      <line x1="32" y1="8" x2="150" y2="8" stroke="var(--brand-red)" stroke-width="1"/>
      <line x1="0" y1="102" x2="120" y2="102" stroke="var(--brand-red)" stroke-width="1"/>
      <text x="130" y="118" font-family="Georgia, serif" font-weight="700" font-size="26" fill="var(--brand-red)">”</text>
    </svg>
    <blockquote class="pull-quote__text">If you fail<br>to plan, you are<br>planning to fail</blockquote>
  </figure>
  <p class="footer-note">© 2020 HarlowBrent&nbsp; Chartered Accountants</p>
  <p class="page-number">3</p>
</section>

<!-- Excel insert -->
<section class="page page--excel">
  <svg class="page__art" viewBox="0 0 413 584" aria-hidden="true">
    <polygon points="230,584 363,495 363,520 268,584" fill="var(--band-grey)"/>
    <polygon points="385,508 413,490 413,512 385,530" fill="var(--band-grey)"/>
    <polygon points="302,584 413,510 413,584" fill="var(--brand-red)"/>
  </svg>
  <div class="wordmark wordmark--small">HARLOW BRENT<span class="wordmark__tag">CHARTERED ACCOUNTANTS</span></div>
  <p class="running-head">2020 Tax Planning | Client Name Here</p>
  <p class="excel-label">Excel sheets added here</p>
  <div class="excel-bar excel-bar--head"></div>
  <div class="excel-bar excel-bar--row"></div>
  <p class="footer-note">© 2020 HarlowBrent&nbsp; Chartered Accountants</p>
  <p class="page-number">4</p>
</section>

<!-- Strategies -->
<section class="page page--strategies">
  <svg class="page__art" viewBox="0 0 413 584" aria-hidden="true">
    <polygon points="230,584 363,495 363,520 268,584" fill="var(--band-grey)"/>
    <polygon points="385,508 413,490 413,512 385,530" fill="var(--band-grey)"/>
    <polygon points="302,584 413,510 413,584" fill="var(--brand-red)"/>
  </svg>
  <div class="wordmark wordmark--small">HARLOW BRENT<span class="wordmark__tag">CHARTERED ACCOUNTANTS</span></div>
  <p class="running-head">2020 Tax Planning | Client Name Here</p>
  <h2 class="strategy-title">Taxation Planning Stratagies<br>Main Taxation Plannings Strategies</h2>
  <p class="strategy-label">Stategy</p>
  <h3 class="caps-head serif" style="top:145px">TAX PLANNING STRATEGIES</h3>
  <p class="caps-note serif" style="top:158px">A more detailed list of potential tax planning strategies is as follows:</p>
  <h3 class="caps-head serif" style="top:187px">MAIN TAX PLANNING STRATEGIES</h3>
  <p class="caps-note serif" style="top:208px">STRATEGY</p>
  <div class="strategy-table serif">
    <div class="strategy-row">
      <h4>Bring Forward Expenses</h4>
      <p>If possible, you should incur any business use expenses prior to 30 JuneT his way that expense will be included in the current tax year rather than NEXT tax year, reducing your tax payable in this financial year.</p>
      <p style="margin-bottom:0">Examples include: consumables, repairs, computer and office supplies.</p>
    </div>
    <div class="strategy-row">
      <h4>Defer Income</h4>
      <p style="margin-bottom:0">If possible, you should defer issuing invoices in the last week or two until after 30 June 2019. This way that income will be included in the 2020 tax year rather than the 2019 tax year, deferring tax on the income for a year. Cash basis taxpayers should defer receipt of payment if possible.</p>
    </div>
    <div class="strategy-row">
      <h4>Accounts Receivable</h4>
      <p style="margin-bottom:0">Under the small business tax concessions, the financial statements can be prepared on a cash basis so amounts receivable can be removed from the financial statements for tax purposes</p>
    </div>
    <div class="strategy-row">
      <h4>Accounts Payable</h4>
      <p>Under the small business tax concessions, the financial statements can be prepared on a cash basis so amounts payable can be removed from the financial statements for tax purposes<br>Depreciation From Purchased Assets that Cost more than $30,000</p>
      <p style="margin-bottom:0">A small business entity that purchases depreciating assets that cost more than:</p>
      <ul>
        <li>-&nbsp;&nbsp;&nbsp;&nbsp;&nbsp;$30,000 from 3 April 2019 - 30 June 2019</li>
        <li>-&nbsp;&nbsp;&nbsp;&nbsp;&nbsp;$25,000 from 29 January 2019 – 2 April 2019</li>
        <li>-&nbsp;&nbsp;&nbsp;&nbsp;&nbsp;$20,000 from 1 July 2018 – 28 January 2019</li>
      </ul>
      <p style="margin-bottom:0">Will receive the following tax deductions from pooling the asset(s) in a small business asset pool:</p>
      <ul style="margin-bottom:10px">
        <li>□&nbsp;&nbsp;&nbsp;&nbsp;A 15% deduction in the 2019 tax year, regardless of when you purchased or acquired the asset during the year; and</li>
        <li>□&nbsp;&nbsp;&nbsp;&nbsp;A 30% deduction each year after the first year.</li>
      </ul>
    </div>
  </div>
  <p class="footer-note">© 2020 HarlowBrent&nbsp; Chartered Accountants</p>
  <p class="page-number">5</p>
</section>

</body>
</html>
```